Duel Business card

Want an edgy business card that shows both of our companies on each side of the card, OR both together with a cool design.

*Must be edgy: We have attached our two business logos. We are a bail bond and immigration bond company.

Would like the address on one side only.
Need Phone, cell, website, address, and Name

Company Name 1: Liberty Release Partners
www.libertyreleasepartners-example.com

Company Name 2: Crossway Custody Advocates
www.crosswaycustodyadvocates-example.com

These cards will need to be easily changeable so I can modify new employees

Target Market(s)

people in jail, takign imigrants out of jail and from being taken back to there country

Industry/Entity Type

Business

Requirements
Must have
• Include both logos attached

```html
<!DOCTYPE html>
<html lang="en">
<head>
<meta charset="utf-8">
<title>Dual Business Card</title>
<link rel="stylesheet" href="https://fonts.googleapis.com/css2?family=Arimo:wght@400;700&display=swap">
<style>
  :root {
    --backdrop: #b3b3b3;
    --card: #ffffff;
    --navy: #0b2f8a;
    --red: #e63327;
    --ink: #333333;
    --shadow: rgba(0, 0, 0, 0.28);
  }
  * { box-sizing: border-box; margin: 0; padding: 0; }
  html, body {
    width: 1200px;
    height: 602px;
    overflow: hidden;
    background: var(--backdrop);
    font-family: "Arimo", Arial, sans-serif;
  }
  .stage { position: relative; width: 1200px; height: 602px; }
  .card {
    position: absolute;
    width: 538px;
    height: 324px;
    background: var(--card);
    transform: scale(0.948);
    transform-origin: top left;
    box-shadow: 0 4px 10px var(--shadow);
    overflow: hidden;
  }
  .card-front { left: 56px; top: 56px; }
  .card-back { left: 634px; top: 238px; }
  .card-shapes { position: absolute; inset: 0; width: 538px; height: 324px; }

  /* front brand marks */
  .brand-mark {
    position: absolute;
    display: flex;
    flex-direction: column;
    align-items: center;
    text-align: center;
    gap: 8px;
  }
  .brand-mark .dot { border-radius: 50%; }
  .brand-mark .name { font-weight: 700; line-height: 1.1; }
  .brand-bail { left: 38px; top: 140px; width: 190px; }
  .brand-bail .dot { width: 36px; height: 36px; background: var(--navy); }
  .brand-bail .name { color: var(--navy); font-size: 19px; }
  .brand-immigration { left: 336px; top: 112px; width: 150px; }
  .brand-immigration .dot { width: 52px; height: 52px; background: var(--red); }
  .brand-immigration .name { color: var(--red); font-size: 17px; }

  /* back details */
  .holder-name {
    position: absolute;
    left: 29px;
    top: 56px;
    font-size: 26px;
    font-weight: 700;
    color: var(--navy);
  }
  .name-rule { position: absolute; left: 29px; top: 86px; width: 480px; height: 3px; display: flex; }
  .name-rule .red { flex: 0 0 241px; background: var(--red); }
  .name-rule .blue { flex: 1; background: var(--navy); }

  .company {
    position: absolute;
    left: 28px;
    width: 490px;
    display: flex;
    align-items: center;
  }
  .company-bail { top: 113px; }
  .company-immigration { top: 201px; }
  .company-mark {
    width: 78px;
    display: flex;
    flex-direction: column;
    align-items: center;
    gap: 3px;
    text-align: center;
  }
  .company-mark .dot { border-radius: 50%; }
  .company-mark .name { font-size: 8px; font-weight: 700; line-height: 1.1; }
  .company-bail .company-mark .dot { width: 18px; height: 18px; background: var(--navy); }
  .company-bail .company-mark .name { color: var(--navy); }
  .company-immigration .company-mark .dot { width: 24px; height: 24px; background: var(--red); }
  .company-immigration .company-mark .name { color: var(--red); }
  .company-info { margin-left: 24px; font-size: 14px; line-height: 16.6px; color: var(--ink); }
  .company-info .title { font-weight: 700; }
  .company-bail .title { color: var(--navy); }
  .company-immigration .title { color: var(--red); }
  .company-info .label { font-weight: 700; font-style: italic; }
</style>
</head>
<body>
<main class="stage">

  <section class="card card-front" aria-label="Card front">
    <svg class="card-shapes" viewBox="0 0 538 324" aria-hidden="true">
      <polygon fill="var(--red)" points="311,0 538,0 538,29 316,29 276,163 262,163"/>
      <polygon fill="var(--navy)" points="262,163 276,163 238,324 0,324 0,296 229,296"/>
    </svg>
    <div class="brand-mark brand-bail">
      <span class="dot"></span>
      <span class="name">Liberty Release Partners</span>
    </div>
    <div class="brand-mark brand-immigration">
      <span class="dot"></span>
      <span class="name">Crossway Custody Advocates</span>
    </div>
  </section>

  <section class="card card-back" aria-label="Card back">
    <svg class="card-shapes" viewBox="0 0 538 324" aria-hidden="true">
      <polygon fill="var(--navy)" points="0,0 310,0 301,29 0,29"/>
      <polygon fill="var(--red)" points="236,295 538,295 538,324 228,324"/>
    </svg>

    <h1 class="holder-name">Daniel Marsh</h1>
    <div class="name-rule"><span class="red"></span><span class="blue"></span></div>

    <div class="company company-bail">
      <div class="company-mark">
        <span class="dot"></span>
        <span class="name">Liberty Release Partners</span>
      </div>
      <div class="company-info">
        <p class="title">Liberty Release Partners Las Vegas</p>
        <p>418 S. Canyon Ridge Ave. Las Vegas, NV 89101</p>
        <p><span class="label">t</span>. 1-888-555-0142 &nbsp; <span class="label">m</span>. 775-555-0187</p>
        <p>www.libertyreleasepartners-example.com</p>
      </div>
    </div>

    <div class="company company-immigration">
      <div class="company-mark">
        <span class="dot"></span>
        <span class="name">Crossway Custody Advocates</span>
      </div>
      <div class="company-info">
        <p class="title">Crossway Custody Advocates Agency, LLC.</p>
        <p>418 S. Canyon Ridge Ave. Las Vegas, NV 89101</p>
        <p><span class="label">t</span>. 877-555-0163 &nbsp; <span class="label">m</span>. 775-555-0187</p>
        <p>www.crosswaycustodyadvocates-example.com</p>
      </div>
    </div>
  </section>

</main>
</body>
</html>
```